Plakat-Design für Stellenanzeige für eine Allgemeinarztpraxis
Perfekte Arbeit - vielen Dank
Zielgruppe
Gemeinde Lindhofen, ein kleine Landgemeinde im Nordosten von Baden-Württemberg mit ca. 3.600 Einwohner sucht für die ortsansässige Allgemeinarztpraxis einen Nachfolger*in. Die optimale Zielgruppe wären ja junge Ärzte - da sich dies wahrscheinlich als schwierig erweist wird an keine spezielle Altersgruppe gedacht.
Aufgabenstellung
Für die Bewerbung soll ein Straßenbanner im Bauzaunformat (340 x 0173 cm) erstellt werden.
Der Slogan könnte: 'Lindhofen sucht einen Arzt' oder ähnlich lauten.
Ein modernes auffälliges Design wäre wünschenswert.

```html
<!DOCTYPE html>
<html lang="de">
<head>
<meta charset="utf-8">
<title>Ärzt*in gesucht – Bauzaunbanner</title>
<link href="https://fonts.googleapis.com/css2?family=Gochi+Hand&family=Merriweather:wght@400;700&display=swap" rel="stylesheet">
<style>
  :root {
    --red-bright: #ee0b0b;
    --red-mid: #cc0000;
    --red-deep: #9c0000;
    --white: #ffffff;
    --ink: #111111;
    --frame: #cfcfcf;
    --steth: #2a2a2a;
    --mask: #9cc9ea;
    --plaster: #e4b58e;
    --syringe: #e6e9ec;
    --pill-yellow: #f4b430;
    --pill-blue: #7fb6dc;
  }
  html, body {
    margin: 0;
    padding: 0;
    width: 1200px;
    height: 458px;
    overflow: hidden;
    background: var(--white);
  }
  .banner {
    position: absolute;
    left: 167px;
    top: 9px;
    width: 865px;
    height: 440px;
    border: 1px solid var(--frame);
    box-sizing: border-box;
    background: var(--white);
    overflow: hidden;
  }
  .banner__stage {
    position: absolute;
    left: 0; top: 0;
    width: 100%;
    height: 329px;
    background: radial-gradient(ellipse 60% 70% at 48% 45%, var(--red-bright) 0%, var(--red-mid) 55%, var(--red-deep) 100%);
  }
  .headline {
    position: absolute;
    left: 168px;
    top: 34px;
    margin: 0;
    font-family: "Gochi Hand", cursive;
    font-weight: 400;
    color: var(--white);
    line-height: 1;
    text-transform: uppercase;
    letter-spacing: 4px;
  }
  .headline__line { display: block; }
  .headline__line--top { font-size: 140px; margin-left: 16px; }
  .headline__line--bottom { font-size: 134px; margin-top: -22px; }
  .prop {
    position: absolute;
    display: block;
  }
  .prop--stethoscope { left: 20px; top: 18px; width: 150px; height: 330px; }
  .prop--mask { left: 680px; top: 30px; width: 185px; height: 150px; }
  .prop--syringe { left: 702px; top: 226px; width: 130px; height: 56px; }
  .prop--plaster { left: 640px; top: 280px; width: 112px; height: 80px; }
  .pill {
    position: absolute;
    border-radius: 50%;
    box-shadow: 2px 3px 4px rgba(0,0,0,0.25);
  }
  .pill--a { left: 46px; top: 54px; width: 16px; height: 12px; background: #f2f2f2; }
  .pill--b { left: 40px; top: 96px; width: 9px; height: 9px; background: var(--pill-blue); }
  .pill--c { left: 720px; top: 30px; width: 14px; height: 14px; background: var(--pill-yellow); }
  .pill--d { left: 694px; top: 58px; width: 9px; height: 9px; background: #e8742a; }
  .pill--e { left: 195px; top: 297px; width: 14px; height: 14px; background: var(--pill-yellow); }
  .pill--f { left: 805px; top: 318px; width: 16px; height: 16px; background: var(--pill-blue); }
  .footer-info {
    position: absolute;
    left: 37px;
    top: 348px;
    font-family: "Merriweather", serif;
    color: var(--ink);
    font-size: 27px;
    line-height: 1.05;
  }
  .footer-info__url { font-size: 28px; font-weight: 700; letter-spacing: -0.4px; }
  .sender {
    position: absolute;
    left: 741px;
    top: 346px;
    width: 100px;
    text-align: center;
    font-family: "Merriweather", serif;
    font-size: 10px;
    letter-spacing: 2px;
    color: var(--ink);
  }
  .sender__dot {
    display: block;
    width: 44px;
    height: 44px;
    margin: 0 auto 5px;
    border-radius: 50%;
    background: var(--red-mid);
  }
</style>
</head>
<body>
  <div class="banner">
    <div class="banner__stage"></div>

    <span class="pill pill--a"></span>
    <span class="pill pill--b"></span>
    <span class="pill pill--c"></span>
    <span class="pill pill--d"></span>
    <span class="pill pill--e"></span>
    <span class="pill pill--f"></span>

    <svg class="prop prop--stethoscope" role="img" aria-label="Illustration eines Stethoskops" viewBox="0 0 150 330">
      <defs>
        <radialGradient id="stethTone" cx="0.5" cy="0.5" r="0.5">
          <stop offset="0" stop-color="var(--steth)" stop-opacity="0.45"/>
          <stop offset="1" stop-color="var(--steth)" stop-opacity="0"/>
        </radialGradient>
      </defs>
      <ellipse cx="75" cy="165" rx="60" ry="160" fill="url(#stethTone)"/>
    </svg>

    <h1 class="headline">
      <span class="headline__line headline__line--top">Ärzt*in</span>
      <span class="headline__line headline__line--bottom">Gesucht</span>
    </h1>

    <svg class="prop prop--mask" role="img" aria-label="Illustration einer medizinischen Maske" viewBox="0 0 185 150">
      <defs>
        <radialGradient id="maskTone" cx="0.55" cy="0.5" r="0.5">
          <stop offset="0" stop-color="var(--mask)" stop-opacity="0.9"/>
          <stop offset="0.7" stop-color="var(--mask)" stop-opacity="0.5"/>
          <stop offset="1" stop-color="var(--mask)" stop-opacity="0"/>
        </radialGradient>
      </defs>
      <ellipse cx="105" cy="75" rx="85" ry="62" fill="url(#maskTone)"/>
    </svg>

    <svg class="prop prop--syringe" role="img" aria-label="Illustration einer Spritze" viewBox="0 0 130 56">
      <defs>
        <radialGradient id="syringeTone" cx="0.5" cy="0.5" r="0.5">
          <stop offset="0" stop-color="var(--syringe)" stop-opacity="0.7"/>
          <stop offset="1" stop-color="var(--syringe)" stop-opacity="0"/>
        </radialGradient>
      </defs>
      <ellipse cx="65" cy="28" rx="62" ry="16" fill="url(#syringeTone)" transform="rotate(22 65 28)"/>
    </svg>

    <svg class="prop prop--plaster" role="img" aria-label="Illustration eines Pflasters" viewBox="0 0 112 80">
      <defs>
        <radialGradient id="plasterTone" cx="0.5" cy="0.5" r="0.5">
          <stop offset="0" stop-color="var(--plaster)" stop-opacity="1"/>
          <stop offset="0.75" stop-color="var(--plaster)" stop-opacity="0.7"/>
          <stop offset="1" stop-color="var(--plaster)" stop-opacity="0"/>
        </radialGradient>
      </defs>
      <ellipse cx="56" cy="40" rx="54" ry="26" fill="url(#plasterTone)" transform="rotate(-22 56 40)"/>
    </svg>

    <div class="footer-info">
      <div class="footer-info__lead">Mehr Infos unter:</div>
      <div class="footer-info__url">gemeinde-lindhofen.de/ArztGesucht</div>
    </div>

    <div class="sender">
      <span class="sender__dot"></span>
      LINDHOFEN
    </div>
  </div>
</body>
</html>
```